Wendleby Choir needs a concert poster!

22nd November is Ss Ottoline's Feast, the Patron Saint of music. 100 years ago on that day, Dorian Maltravers was born, famously dubbed the "greatest English composer since Gadsby". 50 years ago that day, three of the most prominent men in history died: this trifecta included theologian and author of 'Quellmark' R. T. Pembury, philosopher and author of 'Silent Tin Harvest' Perrine Vasholt, and one of America's most beloved presidents, Walter G. Ashcombe.

In memory of these prominent figures of the 20th century, the Choir of Holy Ambrose by the Weir Stile (the Market Kirk of Wendleby) perform some of the world's best vocal music composed or inspired by these men. The playlist includes Maltravers's 'Carol for Ss Ottoline', K. D. Ruhnau's 'Geh, Seele, geh', 'The Lantern' by Perrin Vasholt set to music by Miles Tandridge, and Cuthbert Fennimore's 'Lay down, dear one, in quiet rest', written specially for the memorial service of President Walter G Ashcombe in Harrowgate Federal Minster.

We are looking for a dramatic concert poster / or series of posters that encapsulate all these important aspects on this one day. Tickets will be set up on seatpassly.net - space for their logo will be needed.

22nd November 2013, 8pm
Norbury College Chapel, Oxford
Choir of Holy Ambrose by the Weir Stile
Gil Pettifer-Rowe
Tickets: £5

Target Market(s)

Mostly students and staff from the Universities of Wendleby and Marlowe, but also singers from local Oxfordshire choral societies who have a passion for singing and the repertoire. Local musical professionals and appreciators. Not really suitable for children. Cultured adults that support local artistic projects and go to live classical concerts. Higher-end readership. I would like to charge much more for the ticket prices (in order to reflect the quality of the performance) but Oxford is haemorrhaging quality concerts for very little, and the competition is fierce. This poster needs to stand out from the crowd of other events going on, and perhaps be coupled with an inventive marketing strategy.

Industry/Entity Type

Church

Requirements
Must have
• Holy Ambrose by the Weir Stile logo
Seatpassly.net logo

My name prominently displayed

```html
<!DOCTYPE html>
<html lang="en">
<head>
<meta charset="utf-8">
<title>Choir of Holy Ambrose by the Weir Stile — Concert Poster</title>
<link rel="stylesheet" href="https://fonts.googleapis.com/css2?family=Cinzel:wght@400;700;900&display=swap">
<style>
  :root {
    --navy: #0b1758;
    --deep: #16288a;
    --blue: #2f5fe0;
    --sky: #8fb8ff;
    --violet: #4a2a9e;
    --magenta: #b63be0;
    --pink: #e98cf5;
    --ink: #ffffff;
    --ink-soft: #e4ecff;
    --ticket-bg: #e9f1ff;
    --ticket-ink: #2a3aa8;
  }
  * { margin: 0; padding: 0; box-sizing: border-box; }
  html, body { width: 849px; height: 1200px; overflow: hidden; background: var(--navy); }
  .poster {
    position: relative;
    width: 849px;
    height: 1200px;
    overflow: hidden;
    font-family: "Cinzel", Georgia, serif;
    color: var(--ink);
    background: linear-gradient(180deg, #3b6ff0 0%, var(--blue) 18%, var(--deep) 36%, var(--navy) 50%, var(--deep) 68%, var(--violet) 84%, var(--magenta) 100%);
  }
  .conductor-art {
    position: absolute; left: 0; top: 0; width: 849px; height: 560px;
    background:
      radial-gradient(ellipse 260px 300px at 470px 210px, rgba(200,220,255,0.55), rgba(120,160,255,0.2) 55%, transparent 75%),
      radial-gradient(ellipse 330px 260px at 90px 60px, rgba(190,130,255,0.55), transparent 70%),
      radial-gradient(ellipse 300px 240px at 800px 120px, rgba(90,140,255,0.5), transparent 70%),
      linear-gradient(160deg, #6a92ff 0%, #3a64e6 40%, #2545c0 70%, #16288a 100%);
    -webkit-mask-image: linear-gradient(180deg, #000 0%, #000 62%, transparent 100%);
            mask-image: linear-gradient(180deg, #000 0%, #000 62%, transparent 100%);
  }
  .score-sweep { position: absolute; left: 0; top: 240px; width: 849px; height: 320px; }
  .score-art-lower {
    position: absolute; left: 0; top: 900px; width: 849px; height: 300px;
    background:
      radial-gradient(ellipse 460px 190px at 280px 290px, rgba(240,150,255,0.55), transparent 70%),
      radial-gradient(ellipse 300px 160px at 760px 260px, rgba(200,90,240,0.45), transparent 70%);
  }
  .details { position: absolute; left: 0; width: 100%; text-align: center; }
  .date { top: 500px; font-size: 34px; letter-spacing: 1px; color: var(--ink-soft); }
  .venue { top: 548px; font-size: 27px; letter-spacing: 1px; color: var(--ink-soft); }
  .choir { top: 604px; font-size: 48px; font-weight: 700; letter-spacing: 0.5px; line-height: 1; }
  .choir-sub { display: block; font-size: 25px; font-weight: 700; margin-top: 4px; }
  .programme {
    top: 706px; left: 52px; width: 745px;
    font-size: 16px; font-weight: 700; line-height: 1.6; color: var(--ink-soft);
  }
  .director { top: 806px; font-size: 38px; letter-spacing: 0.5px; }
  .rule { position: absolute; left: 150px; width: 549px; height: 2px; background: rgba(220,232,255,0.75); top: 860px; }
  .tickets {
    position: absolute; right: 16px; top: 888px;
    padding: 6px 16px; background: var(--ticket-bg);
    color: var(--ticket-ink); font-size: 26px; font-weight: 700;
    border-radius: 4px;
  }
  .partners { position: absolute; left: 0; width: 100%; top: 1112px; display: flex; justify-content: center; gap: 46px; align-items: center; }
  .partner { display: flex; align-items: center; gap: 10px; font-size: 19px; font-weight: 700; color: var(--ink); }
  .partner-mark { width: 30px; height: 30px; background: var(--ink); }
</style>
</head>
<body>
<main class="poster">
  <div class="conductor-art" role="img" aria-label="Photograph of a conductor with raised arms in blue light"></div>
  <svg class="score-sweep" viewBox="0 0 849 320" role="img" aria-label="Sheet music pages swept across the poster">
    <defs>
      <linearGradient id="sweep" x1="0" y1="0" x2="1" y2="0">
        <stop offset="0" stop-color="#9ec0ff" stop-opacity="0.05"/>
        <stop offset="0.5" stop-color="#b9d0ff" stop-opacity="0.28"/>
        <stop offset="1" stop-color="#9ec0ff" stop-opacity="0.08"/>
      </linearGradient>
    </defs>
    <path d="M0 150 C 250 60, 560 60, 849 20 L 849 130 C 560 170, 260 190, 0 260 Z" fill="url(#sweep)"/>
    <path d="M0 150 C 250 60, 560 60, 849 20" fill="none" stroke="#d6e4ff" stroke-opacity="0.35" stroke-width="2"/>
  </svg>
  <div class="score-art-lower" role="img" aria-label="Sheet music glowing in purple and pink light"></div>

  <p class="details date">22nd November 2013, 8pm</p>
  <p class="details venue">Norbury College Chapel, Oxford</p>
  <h1 class="details choir">Choir of Holy Ambrose<span class="choir-sub">by the Weir Stile</span></h1>
  <p class="details programme">Maltravers's 'Carol for Ss Ottoline', K. D. Ruhnau's 'Geh, Seele, geh', 'The Lantern' by Perrin Vasholt set to music by Miles Tandridge, Cuthbert Fennimore's 'Lay down, dear one, in quiet rest' and more!</p>

  <h2 class="details director">Gil Pettifer-Rowe</h2>
  <div class="rule"></div>

  <p class="tickets">Tickets: £5</p>

  <div class="partners">
    <div class="partner"><span class="partner-mark"></span>Holy Ambrose</div>
    <div class="partner">Seatpassly.net</div>
  </div>
</main>
</body>
</html>
```